Bricks in the Wall

We need graphics for a 5x7 or 6x9 post card, single sided for a small speech language pathology practice that serves pediatric patients primarily with children on the autism spectrum.

I want a brick wall, with words and phrases written into the bricks. (to follow)
A child standing on top of the wall with hands up in success.
A few incomplete autism puzzles on the ground.
A larger complete autism puzzle in the the child's hand.
The title is: Speech/Language Therapy
The Foundation for Communication Success
Words/phrases to go into the red bricks:
Receptive Language, Expressive Language, Pragmatics, Sensory, cognitive,
social language, autism, articulation, TeleTherapy, auditory processing, screening, evaluation, developmental delay, Goals, family involvement, environmental communication, ASD, Mirror Neurons.
Updates

Target Market(s)

Children with speech and language disorders.

Industry/Entity Type

Speech and Language Therapy

Font styles to use
Serif

Requirements
Must have
• Colors, primary and red bricks.
Nice to have
• I want the postcard to have a happy feel to it and a sense of success.
Should not have
• I don't want it cluttered.

```html
<!DOCTYPE html>
<html lang="en">
<head>
<meta charset="utf-8">
<title>Speech/Language Therapy – The Foundation for Communication Success</title>
<link rel="stylesheet" href="https://fonts.googleapis.com/css2?family=Alfa+Slab+One&display=swap">
<style>
  :root {
    --orange: #f5a41d;
    --rust: #d9612a;
    --brick-red: #c8372d;
    --ink: #2f2a28;
    --slate: #2d3b47;
    --white: #ffffff;
    --steel: #cfd2d4;
  }
  html, body {
    margin: 0;
    padding: 0;
    width: 1200px;
    height: 869px;
    overflow: hidden;
    background: var(--white);
  }
  .postcard {
    display: block;
    width: 1200px;
    height: 869px;
  }
  .title,
  .brick-label,
  .caption {
    font-family: "Alfa Slab One", "Rockwell", serif;
  }
  .title { fill: var(--ink); text-anchor: end; }
  .title-lead { font-size: 52px; }
  .title-sub { font-size: 30px; }
  .brick { fill: var(--brick-red); }
  .brick-outlined { stroke: var(--white); stroke-width: 3; }
  .brick-label {
    fill: var(--white);
    font-size: 21px;
    text-anchor: middle;
    dominant-baseline: central;
  }
  .caption {
    fill: var(--ink);
    font-size: 30px;
    text-anchor: middle;
  }
  .pointer {
    fill: none;
    stroke: var(--slate);
    stroke-width: 7;
    stroke-linecap: round;
    stroke-linejoin: round;
  }
</style>
</head>
<body>
<svg class="postcard" viewBox="0 0 1214 867" preserveAspectRatio="none" xmlns="http://www.w3.org/2000/svg">
  <!-- background bands -->
  <rect class="band-top" x="0" y="0" width="1214" height="264" fill="var(--orange)"/>
  <rect class="band-middle" x="0" y="264" width="1214" height="603" fill="var(--white)"/>
  <polygon class="band-bottom" points="0,857 1214,575 1214,867 0,867" fill="var(--orange)"/>
  <polygon class="band-stripe" points="0,850 1214,568 1214,582 0,864" fill="var(--rust)"/>

  <!-- puzzle cluster -->
  <rect class="puzzle-cluster" x="134" y="62" width="130" height="130" rx="10" fill="var(--rust)" opacity="0.55" role="img" aria-label="Cluster of four interlocking puzzle pieces"/>

  <!-- title -->
  <text class="title title-lead" x="1140" y="100">Speech/Language Therapy</text>
  <text class="title title-sub" x="1140" y="158">The Foundation for Communication Success</text>

  <!-- row 1 -->
  <polygon class="brick" points="73,232 357,232 332,317 73,317"/>
  <text class="brick-label" x="208" y="275">Receptive Language</text>
  <polygon class="brick" points="529,232 637,232 637,317 509,317"/>
  <text class="brick-label" x="577" y="275">Autism</text>
  <rect class="brick" x="670" y="232" width="295" height="85"/>
  <text class="brick-label" x="817" y="275">Expressive Language</text>
  <rect class="brick" x="1007" y="232" width="133" height="85"/>
  <text class="brick-label" x="1073" y="275">Goals</text>

  <!-- row 2 -->
  <rect class="brick" x="126" y="348" width="133" height="82"/>
  <text class="brick-label" x="192" y="389">Sensory</text>
  <rect class="brick" x="495" y="348" width="195" height="82"/>
  <text class="brick-label" x="592" y="389">Pragmatics</text>
  <rect class="brick" x="720" y="348" width="180" height="82"/>
  <text class="brick-label" x="810" y="389">Evaluation</text>
  <rect class="brick" x="930" y="348" width="210" height="82"/>
  <text class="brick-label" x="1035" y="389">Articulation</text>

  <!-- row 3 -->
  <rect class="brick" x="74" y="461" width="113" height="82"/>
  <text class="brick-label" x="130" y="502"><tspan x="130" dy="-12">Mirror</tspan><tspan x="130" dy="25">Neurons</tspan></text>
  <polygon class="brick" points="226,461 289,461 266,543 226,543"/>
  <rect class="brick" x="495" y="461" width="145" height="82"/>
  <text class="brick-label" x="567" y="502">Screening</text>
  <rect class="brick" x="670" y="461" width="295" height="82"/>
  <text class="brick-label" x="817" y="502">Auditory Processing</text>
  <rect class="brick" x="995" y="461" width="145" height="82"/>
  <text class="brick-label" x="1067" y="502">Cognitive</text>

  <!-- row 4 -->
  <polygon class="brick" points="74,574 264,574 243,656 74,656"/>
  <text class="brick-label" x="158" y="615">TeleTherapy</text>
  <rect class="brick" x="495" y="574" width="215" height="82"/>
  <text class="brick-label" x="602" y="615"><tspan x="602" dy="-12">Social</tspan><tspan x="602" dy="25">Language</tspan></text>
  <rect class="brick" x="739" y="574" width="80" height="82"/>
  <text class="brick-label" x="779" y="615">ASD</text>
  <rect class="brick brick-outlined" x="846" y="574" width="295" height="82"/>
  <text class="brick-label" x="993" y="615"><tspan x="993" dy="-12">Environmental</tspan><tspan x="993" dy="25">Communication</tspan></text>

  <!-- ladder -->
  <polygon class="ladder" points="430,200 500,200 392,727 312,727" fill="var(--steel)" role="img" aria-label="Metal ladder leaning against the brick wall"/>

  <!-- pointer -->
  <path class="pointer" d="M622,772 C600,830 520,840 470,815 C410,785 420,710 470,722 C505,732 470,790 420,770 C370,748 345,710 330,675"/>
  <path class="pointer" d="M310,705 L327,668 L358,690"/>

  <!-- caption -->
  <text class="caption" x="852" y="762">Child on first step, Reaching of</text>
  <text class="caption" x="852" y="802">with hand on next ring</text>
</svg>
</body>
</html>
```